We need a card design for our company Harbor Lantern Partners. Our goal is to save people money on their disposal services. For this post card please put our logo in it. Please use these colors Pantone 576c and 418c or green and grey. We are giving you as the designer the opportunity to be creative with any other images. We are looking to have a fun eye catching postcard.
Please write:
Think you are stuck with your trash bill? Think again
We cut your neighbors disposal cost by 40%.

Please put down our information also,
Contact us
800.514.7262
melinda@plumcrest782.com
plumcrest782.com

```html
<!DOCTYPE html>
<html lang="en">
<head>
<meta charset="utf-8">
<title>Harbor Lantern Partners Postcard</title>
<link rel="stylesheet" href="https://fonts.googleapis.com/css2?family=Open+Sans:wght@400;600;800&display=swap">
<style>
  :root {
    --page-bg: #e9e7e3;
    --card-green: #7fb450;
    --deep-green: #2f6a2e;
    --brand-green: #7aab3e;
    --ink-grey: #55585a;
    --band-white: #ffffff;
    --text-white: #ffffff;
  }
  * { box-sizing: border-box; margin: 0; padding: 0; }
  html, body {
    width: 1200px;
    height: 1028px;
    overflow: hidden;
    background: var(--page-bg);
    font-family: "Open Sans", sans-serif;
  }
  .postcard {
    position: absolute;
    left: 50px;
    top: 180px;
    width: 1100px;
    height: 667px;
    background: var(--card-green);
    box-shadow: 0 10px 30px rgba(0,0,0,0.18);
    overflow: hidden;
  }
  .teaser {
    position: absolute;
    left: 88px;
    top: 78px;
    color: var(--text-white);
    font-size: 27px;
    line-height: 1.4;
    font-weight: 400;
  }
  .claim {
    position: absolute;
    left: 88px;
    top: 198px;
    color: var(--text-white);
    font-size: 38px;
    line-height: 1.22;
    font-weight: 400;
  }
  .savings-stamp {
    position: absolute;
    left: 428px;
    top: 262px;
    width: 300px;
    height: 128px;
    border: 7px solid var(--deep-green);
    border-radius: 18px;
    color: var(--deep-green);
    font-size: 104px;
    font-weight: 800;
    line-height: 114px;
    text-align: center;
    letter-spacing: -2px;
  }
  .recycle-art {
    position: absolute;
    right: 92px;
    top: 34px;
    width: 230px;
    height: 210px;
    background: radial-gradient(circle, #3f7a34 0%, #5e9640 70%, var(--card-green) 100%);
    border-radius: 50%;
    opacity: 0.85;
  }
  .contact-band {
    position: absolute;
    left: 0;
    bottom: 0;
    width: 100%;
    height: 132px;
    background: var(--band-white);
  }
  .brand {
    position: absolute;
    left: 80px;
    top: 46px;
    display: flex;
    align-items: center;
    gap: 12px;
  }
  .brand-mark {
    width: 22px;
    height: 22px;
    background: var(--brand-green);
  }
  .brand-name {
    color: var(--brand-green);
    font-size: 25px;
    font-weight: 600;
  }
  .contact {
    position: absolute;
    left: 480px;
    top: 4px;
    width: 560px;
    color: var(--ink-grey);
  }
  .contact-prompt {
    font-size: 21px;
    line-height: 1;
  }
  .contact-phone {
    color: var(--brand-green);
    font-size: 70px;
    font-weight: 400;
    line-height: 1;
    letter-spacing: 1px;
  }
  .contact-lines {
    display: flex;
    justify-content: space-between;
    font-size: 20px;
    margin-top: 2px;
  }
</style>
</head>
<body>
  <main class="postcard">
    <p class="teaser">Think you are stuck with your trash bill?<br>... Think again</p>
    <p class="claim">We cut your neighbors<br>disposal cost by</p>
    <div class="savings-stamp">40%</div>
    <div class="recycle-art" role="img" aria-label="Large recycling arrows emblem in dark green"></div>

    <footer class="contact-band">
      <div class="brand">
        <span class="brand-mark"></span>
        <span class="brand-name">Harbor Lantern Partners</span>
      </div>
      <div class="contact">
        <p class="contact-prompt">ask us how...</p>
        <p class="contact-phone">800 514 7262</p>
        <div class="contact-lines">
          <span>melinda@plumcrest782.com</span>
          <span>www.plumcrest782.com</span>
        </div>
      </div>
    </footer>
  </main>
</body>
</html>
```